New Business Card Design Project for Handyman Business

I would like to purchase a customized version of a design you have previously submitted - https://www.plimvaro.example/work/58302716
I love this design!
I am hoping you can design something similar to this for our Handyman Business.
Attached is our logo and some graphics we have used.
Here is a link to the Google Doc with the content that needs to be included, https://files.trenowick.example/sheet/q/4XRKW-7hLp2DnQv8sTc5ma-ZzoeB3kWu9YyTgp6HJ__RmwNdVcQeLbs4jfnv0ztqxhaK7M41p9ggWHe/view
Target Market(s)
Real Estate Agents, Home Owners and Property Managers
Industry/Entity Type
Construction/ Speciality Trade
Contact Information for Business Card
https://files.trenowick.example/sheet/7QpaRzN_ukoyb4cXTwLHhJe8KnuSbPjCr2QDaLy6nwod/view?mode=shared
Font styles to use
Other font styles liked:
- Ubuntu
Look and feel
Each slider illustrates characteristics of the customer's brand and the style your logo design should communicate.

```html
<!DOCTYPE html>
<html lang="en">
<head>
<meta charset="utf-8">
<title>Tidewell Business Card</title>
<link href="https://fonts.googleapis.com/css2?family=Ubuntu:wght@400;500;700&display=swap" rel="stylesheet">
<style>
  :root {
    --bg: #2b2b2d;
    --card: #1d1d1f;
    --blue: #1a83d4;
    --green: #3cbd4a;
    --orange: #f07236;
    --white: #f4f4f4;
    --rule: #5a5a5e;
    --pattern: #262628;
  }
  * { box-sizing: border-box; margin: 0; padding: 0; }
  html, body { width: 1200px; height: 1108px; overflow: hidden; }
  body {
    background: var(--bg);
    font-family: "Ubuntu", sans-serif;
    position: relative;
  }
  .card {
    position: absolute;
    top: 194px;
    width: 420px;
    height: 720px;
    background: var(--card);
    border-radius: 26px;
    overflow: hidden;
  }
  .card--front { left: 150px; }
  .card--back { left: 630px; }

  .front { display: flex; flex-direction: column; align-items: center; padding-top: 92px; text-align: center; }
  .brand__name { font-size: 50px; font-weight: 500; color: var(--white); line-height: 1; }

  .person { margin-top: 76px; }
  .person__name { font-size: 34px; letter-spacing: 1px; }
  .person__first { color: var(--blue); font-weight: 400; }
  .person__last { color: var(--green); font-weight: 700; }
  .person__role { color: var(--white); font-size: 19px; margin-top: 4px; }

  .contact-rule { width: 330px; display: flex; align-items: center; gap: 10px; margin-top: 18px; }
  .contact-rule::before, .contact-rule::after { content: ""; flex: 1; height: 1px; background: var(--rule); }
  .contact-icons { display: flex; gap: 6px; }
  .contact-icon { width: 30px; height: 30px; border-radius: 4px; display: flex; align-items: center; justify-content: center; }
  .contact-icon--phone { background: var(--blue); }
  .contact-icon--mail { background: var(--green); }
  .contact-icon--web { background: var(--orange); }

  .contact { color: var(--white); font-size: 17px; line-height: 1.45; margin-top: 10px; }
  .contact__site-a { color: var(--blue); }
  .contact__site-b { color: var(--green); }
  .contact__site-c { color: var(--orange); }

  .rule { width: 330px; height: 1px; background: var(--rule); margin: 14px 0; }
  .services { color: var(--white); font-size: 19px; line-height: 1.25; }
  .services__list { color: var(--blue); font-size: 17px; margin-top: 12px; }

  .social { display: flex; gap: 14px; margin-top: 2px; }
  .social__box { width: 36px; height: 36px; border: 2px solid var(--white); border-radius: 5px; }
  .hashtag { color: var(--white); font-size: 18px; margin-top: 22px; line-height: 1.3; }

  .back__pattern {
    position: absolute; inset: 0;
    background: linear-gradient(160deg, #222224 0%, var(--pattern) 50%, #1f1f21 100%);
  }
  .back__brand { position: absolute; left: 0; right: 0; bottom: 96px; text-align: center; }
  .back__name { font-size: 34px; font-weight: 500; color: var(--white); line-height: 1; }
</style>
</head>
<body>
  <section class="card card--front">
    <div class="front">
      <div class="brand">
        <div class="brand__name">tidewell</div>
      </div>

      <div class="person">
        <div class="person__name"><span class="person__first">MARLO</span> <span class="person__last">QUENBY</span></div>
        <div class="person__role">Owner/ Handyman</div>
      </div>

      <div class="contact-rule">
        <div class="contact-icons">
          <div class="contact-icon contact-icon--phone">
            <svg width="18" height="18" viewBox="0 0 24 24" aria-hidden="true"><path d="M6.6 10.8a15 15 0 0 0 6.6 6.6l2.2-2.2a1 1 0 0 1 1-.25 11.4 11.4 0 0 0 3.6.57 1 1 0 0 1 1 1V20a1 1 0 0 1-1 1A17 17 0 0 1 3 4a1 1 0 0 1 1-1h3.5a1 1 0 0 1 1 1c0 1.25.2 2.45.57 3.57a1 1 0 0 1-.25 1z" fill="#fff"/></svg>
          </div>
          <div class="contact-icon contact-icon--mail">
            <svg width="20" height="16" viewBox="0 0 20 16" aria-hidden="true"><rect x="1" y="1" width="18" height="14" fill="none" stroke="#fff" stroke-width="2"/><path d="M1 1l9 8 9-8" fill="none" stroke="#fff" stroke-width="2"/></svg>
          </div>
          <div class="contact-icon contact-icon--web">
            <svg width="20" height="20" viewBox="0 0 20 20" aria-hidden="true"><g fill="none" stroke="#fff" stroke-width="1.5"><circle cx="10" cy="10" r="8"/><ellipse cx="10" cy="10" rx="3.5" ry="8"/><path d="M2 10h16M3.5 6h13M3.5 14h13"/></g></svg>
          </div>
        </div>
      </div>

      <div class="contact">
        <div>(555) 014-2738</div>
        <div>marlo@tidewell.example</div>
        <div><span class="contact__site-a">Tidewell</span><span class="contact__site-b">.</span><span class="contact__site-c">example</span></div>
      </div>

      <div class="rule"></div>
      <div class="services">Commercial and Residential<br>Handyman</div>
      <div class="services__list">Improve • Repair • Remodel • Maintain</div>
      <div class="rule"></div>

      <div class="social">
        <div class="social__box"></div>
        <div class="social__box"></div>
        <div class="social__box"></div>
        <div class="social__box"></div>
      </div>
      <div class="hashtag">#TidewellHandyman<br>Services</div>
    </div>
  </section>

  <section class="card card--back">
    <div class="back__pattern" role="img" aria-label="Faint repeated brand name pattern across the card back"></div>
    <div class="back__brand">
      <div class="back__name">tidewell</div>
    </div>
  </section>
</body>
</html>
```